Realty Group Needs Classy, Contemporary Letterhead Design

We need a letterhead design for a new realty company located in NY, USA. We buy investment properties to rehabilitate and or keep in our rental portfolio.

```html
<!DOCTYPE html>
<html lang="en">
<head>
<meta charset="utf-8">
<title>Meridian Realty Group Letterhead</title>
<link href="https://fonts.googleapis.com/css2?family=Open+Sans:wght@400;600&family=Montserrat:wght@800&family=Lato:wght@400&display=swap" rel="stylesheet">
<style>
  :root {
    --purple: #4f2a87;
    --purple-deep: #3f2070;
    --rule-gray: #7d7d80;
    --ink: #3d3d3d;
    --ink-dark: #2b2b2b;
    --paper: #ffffff;
    --backdrop: #e6e6e8;
    --white: #ffffff;
  }
  * { margin: 0; padding: 0; box-sizing: border-box; }
  html, body { width: 1040px; height: 1200px; overflow: hidden; background: var(--backdrop); }
  .letterhead {
    position: absolute; left: 54px; top: 0;
    width: 932px; height: 1200px;
    background: var(--paper);
    font-family: "Open Sans", sans-serif;
    color: var(--ink);
  }
  .brand {
    position: absolute; left: 563px; top: 24px; width: 266px;
    text-align: center; color: var(--purple);
    font-family: "Montserrat", sans-serif; font-weight: 800;
  }
  .brand-name { display: block; font-size: 44px; line-height: 50px; letter-spacing: -1px; }
  .brand-sub { display: block; font-size: 14px; line-height: 18px; letter-spacing: 1px; }
  .content { position: absolute; left: 88px; width: 754px; font-size: 15px; }
  .issue-date { top: 217px; line-height: 20px; }
  .recipient { top: 254px; line-height: 18px; }
  .salutation { top: 357px; line-height: 20px; }
  .body-copy { top: 406px; line-height: 27px; text-align: justify; }
  .body-copy p + p { margin-top: 27px; }
  .closing { top: 815px; line-height: 20px; }
  .signature {
    position: absolute; left: 88px; top: 857px; width: 215px; height: 24px;
    background: linear-gradient(90deg, rgba(60,60,60,0.35), rgba(60,60,60,0.12));
    border-radius: 12px;
  }
  .signer { position: absolute; left: 88px; top: 892px; }
  .signer-name { font-size: 18px; font-weight: 600; color: var(--ink-dark); line-height: 24px; }
  .signer-title { font-size: 15px; line-height: 20px; margin-top: 5px; }
  .footer-rule { position: absolute; left: 0; top: 1101px; width: 100%; height: 8px; background: var(--rule-gray); }
  .footer {
    position: absolute; left: 0; top: 1109px; width: 100%; height: 91px;
    background: var(--purple);
    font-family: "Lato", sans-serif; font-size: 18px; color: var(--white);
  }
  .contact-row { position: absolute; left: 60px; display: flex; align-items: center; height: 30px; }
  .contact-row.address { top: 11px; }
  .contact-row.lines { top: 46px; }
  .contact-item { display: flex; align-items: center; margin-right: 4px; }
  .contact-item svg { width: 28px; height: 28px; margin-right: 6px; flex: none; }
</style>
</head>
<body>
<main class="letterhead">
  <header class="brand">
    <span class="brand-name">MERIDIAN</span>
    <span class="brand-sub">Realty Group, LLC</span>
  </header>

  <div class="content issue-date">Issuing Date: May 5, 2018</div>
  <div class="content recipient">
    Name Of Employee Mr. XYZABC<br>Address of Employee<br>Address Line 2 etc..
  </div>
  <div class="content salutation">Dear Mr.XYZABC</div>

  <section class="content body-copy">
    <p>Lorem Ipsum has been the industry's standard dummy text ever since the 1500s, when an unknown printer took a galley of type and scrambled it to make a type specimen book. It has survived not only five centuries, but also the leap into electronic typesetting, remaining essentially unchanged. It was popularised in the 1960s with the release of Transfera sheets containing Lorem Ipsum passages, and more recently with desktop publishing software like Folio Layout including versions of Lorem Ipsum.</p>
    <p>Lorem Ipsum is simply dummy text of the printing and typesetting industry. Lorem Ipsum has been the industry's standard dummy text ever since the 1500s, when an unknown printer took a galley of type and scrambled it to make a type specimen book.</p>
    <p>It has survived not only five centuries, but also the leap into electronic typesetting, remaining essentially unchanged. It was popularised in the 1960s with the release of Transfera sheets containing Lorem IpsumIpsum passages.</p>
  </section>

  <div class="content closing">Yours Sincerely</div>
  <div class="signature" role="img" aria-label="Handwritten signature of Daniel Whitmore"></div>
  <div class="signer">
    <div class="signer-name">Daniel Whitmore</div>
    <div class="signer-title">Managing Director</div>
  </div>

  <div class="footer-rule"></div>
  <footer class="footer">
    <div class="contact-row address">
      <span class="contact-item">
        <svg viewBox="0 0 28 28" aria-hidden="true"><circle cx="14" cy="14" r="14" fill="#fff"/><path d="M14 6a5.5 5.5 0 0 0-5.5 5.5C8.5 15.5 14 22 14 22s5.5-6.5 5.5-10.5A5.5 5.5 0 0 0 14 6z" fill="var(--purple)"/><circle cx="14" cy="11.5" r="2.2" fill="#fff"/></svg>
        88 Harbor Lane, New York, NY 10012
      </span>
    </div>
    <div class="contact-row lines">
      <span class="contact-item">
        <svg viewBox="0 0 28 28" aria-hidden="true"><circle cx="14" cy="14" r="14" fill="#fff"/><path d="M10 7.5l2.6 3.4-1.6 1.8c.9 2 2.4 3.5 4.3 4.4l1.8-1.6 3.4 2.6-1.5 2.4c-5.3-.4-9.8-4.9-10.3-10.4z" fill="var(--purple)"/></svg>
        212-555 018 734
      </span>
      <span class="contact-item">
        <svg viewBox="0 0 28 28" aria-hidden="true"><circle cx="14" cy="14" r="14" fill="#fff"/><rect x="7.5" y="9" width="13" height="10" rx="1" fill="var(--purple)"/><path d="M8 10l6 5 6-5" stroke="#fff" stroke-width="1.3" fill="none"/></svg>
        hello@meridianrg.com
      </span>
      <span class="contact-item">
        <svg viewBox="0 0 28 28" aria-hidden="true"><circle cx="14" cy="14" r="14" fill="#fff"/><circle cx="14" cy="14" r="6.5" fill="var(--purple)"/><path d="M7.5 14h13M14 7.5c2.5 2.5 2.5 10.5 0 13M14 7.5c-2.5 2.5-2.5 10.5 0 13" stroke="#fff" stroke-width="1" fill="none"/></svg>
        www.meridianrg.com
      </span>
    </div>
  </footer>
</main>
</body>
</html>
```